Popular Australian based wellbeing and high performance podcast needs a design

I need a new, fresh design for my Keep Rising Bright podcast image. This podcast helps and enables its listeners to do their life even better by enhancing their wellbeing, mindset, happiness and leadership. I would love to see designs that include the colour blue. The final design should communicate optimism, hope, approachability and credibility.

Target Market(s)

Target is teenagers to adults wanting to enhance their wellbeing, mindset and happiness.

Font styles to use
Other font styles liked:
• Proba Pro

Colors
33a6d7
0592cd
ffffff

Requirements
Must have
• Must include: Keep Rising Bright podcast
Nice to have
• Could include: with Miles Tervick.

```html
<!DOCTYPE html>
<html lang="en">
<head>
<meta charset="UTF-8">
<title>Keep Rising Bright with Miles Tervick</title>
<link rel="stylesheet" href="https://fonts.googleapis.com/css2?family=Montserrat:ital,wght@0,800;1,500&display=swap">
<style>
  :root {
    --glow: #2fa2f2;
    --mid-blue: #1c6fd0;
    --deep-blue: #0a2a6e;
    --band-navy: #0b2667;
    --band-edge: #081d52;
    --white: #ffffff;
    --host-blue: #6bbaf5;
    --portrait-light: #4f8fd6;
    --portrait-dark: #2a4f93;
  }
  html, body {
    margin: 0;
    padding: 0;
    overflow: hidden;
    background: var(--deep-blue);
  }
  .cover {
    position: relative;
    width: 1200px;
    height: 1200px;
    overflow: hidden;
    background: radial-gradient(circle at 50% 50%, var(--glow) 0%, var(--mid-blue) 42%, var(--deep-blue) 80%);
    font-family: "Montserrat", Arial, sans-serif;
  }
  .lower-band {
    position: absolute;
    left: 0;
    top: 846px;
    width: 1200px;
    height: 354px;
    background: linear-gradient(180deg, var(--band-navy) 0%, var(--band-edge) 100%);
  }
  .host-portrait {
    position: absolute;
    left: 318px;
    top: 258px;
    width: 570px;
    height: 702px;
    border-radius: 220px 220px 24px 24px;
    background: linear-gradient(180deg, var(--portrait-light) 0%, var(--portrait-dark) 100%);
  }
  .show-title {
    position: absolute;
    left: 0;
    top: 0;
    width: 1200px;
    height: 1200px;
  }
  .show-title text {
    font-family: "Montserrat", Arial, sans-serif;
    font-weight: 800;
    font-size: 128px;
    fill: var(--white);
  }
  .host-line {
    position: absolute;
    left: 0;
    top: 1000px;
    width: 1200px;
    margin: 0;
    text-align: center;
    font-family: "Montserrat", Arial, sans-serif;
    font-style: italic;
    font-weight: 500;
    font-size: 90px;
    line-height: 110px;
    color: var(--host-blue);
  }
</style>
</head>
<body>
  <main class="cover">
    <div class="lower-band"></div>
    <div class="host-portrait" role="img" aria-label="Portrait of the host in a blue shirt, leaning forward with hands clasped"></div>
    <svg class="show-title" viewBox="0 0 1200 1200" xmlns="http://www.w3.org/2000/svg" aria-label="Keep Rising Bright">
      <defs>
        <path id="title-arc" d="M 80 744 A 520 520 0 0 1 1120 744"/>
      </defs>
      <text>
        <textPath href="#title-arc" startOffset="50%" text-anchor="middle">Keep Rising Bright</textPath>
      </text>
    </svg>
    <p class="host-line">with Miles Tervick</p>
  </main>
</body>
</html>
```